Aged Care Consultancy Business needs a business card design

I need a two sided business card - I want it clean and professional. Surprise me

Target Market(s)

middle aged and ageing victorians

Industry/Entity Type

Health Care

Contact Information for Business Card

Text to be included

Logo
Aged Care Consulting Services
Professional, Reliable, Affordable

Orin Tessaldo
Director
0472 31 64 09 (larger)
1300 31 64 09
orin@valtrino.com.au
www.valtrinocare.com.au
Facebook (details TBA)

include little icons beside the contact info:

- Envelope = email
- Phone = phone
- Globe = website

Font styles to use
Serif
Sans Serif

Requirements
Must have
• look proffesional and clean

```html
<!DOCTYPE html>
<html lang="en">
<head>
<meta charset="utf-8">
<title>Valtrino Care – Business Card</title>
<link rel="stylesheet" href="https://fonts.googleapis.com/css2?family=Montserrat:wght@400;500;700;800&family=Varela+Round&display=swap">
<style>
  :root {
    --brand-blue: #1f5aa6;
    --brand-blue-deep: #174a8c;
    --brand-blue-light: #2a68b8;
    --brand-yellow: #f0b62b;
    --ink-grey: #6b6b6b;
    --card-white: #f7f7f5;
    --stage: #e6e4df;
    --rule: #f3cf7a;
  }
  * { box-sizing: border-box; margin: 0; padding: 0; }
  html, body { width: 1200px; height: 780px; overflow: hidden; }
  body {
    background: var(--stage);
    font-family: "Montserrat", Arial, sans-serif;
    position: relative;
  }

  .card {
    position: absolute;
    border-radius: 22px;
    overflow: hidden;
    box-shadow: 0 10px 28px rgba(0,0,0,.18);
  }

  /* Front: portrait */
  .card-front {
    left: 110px; top: 110px;
    width: 360px; height: 560px;
    background: var(--card-white);
    display: flex; flex-direction: column; align-items: center;
  }
  .brand {
    display: flex; align-items: center; gap: 12px;
    margin-top: 70px;
  }
  .brand-dot {
    width: 30px; height: 30px; border-radius: 50%;
    background: var(--brand-yellow);
  }
  .brand-name {
    font-family: "Varela Round", Arial, sans-serif;
    font-size: 44px; color: var(--brand-blue);
    letter-spacing: 1px; line-height: 1;
  }
  .person { text-align: center; margin-top: 50px; }
  .person-name {
    font-weight: 800; font-size: 22px; letter-spacing: 1px;
    color: var(--brand-blue);
  }
  .person-name .surname { color: var(--brand-yellow); }
  .person-role { font-size: 16px; color: var(--ink-grey); margin-top: 2px; }

  .contacts { width: 290px; margin-top: 26px; }
  .contact {
    border-top: 1px solid var(--rule);
    padding: 10px 0 12px;
    display: flex; flex-direction: column; align-items: center; gap: 6px;
    color: var(--ink-grey);
  }
  .contact-icon {
    width: 20px; height: 20px; border-radius: 4px;
    background: var(--brand-yellow);
    display: flex; align-items: center; justify-content: center;
  }
  .contact-icon svg { width: 13px; height: 13px; }
  .contact-email { font-size: 16px; }
  .phone-main { font-size: 23px; font-weight: 500; line-height: 1.05; }
  .phone-alt { font-size: 17px; line-height: 1.05; }
  .contact-social { font-size: 16px; }

  .front-band {
    position: absolute; left: 0; right: 0; bottom: 0; height: 72px;
    background: var(--brand-blue);
    border-top: 3px solid var(--brand-yellow);
    display: flex; align-items: center; justify-content: center;
    color: #fff; font-size: 17px; letter-spacing: .5px;
  }

  /* Back: landscape */
  .card-back {
    left: 540px; top: 220px;
    width: 560px; height: 340px;
    background: radial-gradient(circle at 60% 40%, var(--brand-blue-light), var(--brand-blue-deep) 75%);
    display: flex; flex-direction: column; align-items: center; justify-content: center;
    color: #fff;
  }
  .card-back .brand { margin-top: 0; }
  .card-back .brand-name { color: #fff; font-size: 54px; }
  .tagline {
    margin-top: 24px; text-align: center;
    font-size: 16px; line-height: 1.5; letter-spacing: .3px;
  }
</style>
</head>
<body>

  <section class="card card-front" aria-label="Business card front">
    <div class="brand">
      <span class="brand-dot"></span>
      <span class="brand-name">valtrino care</span>
    </div>

    <div class="person">
      <p class="person-name">ORIN <span class="surname">TESSALDO</span></p>
      <p class="person-role">Director</p>
    </div>

    <div class="contacts">
      <div class="contact">
        <span class="contact-icon">
          <svg viewBox="0 0 16 16"><rect x="1.5" y="3.5" width="13" height="9" rx="1" fill="none" stroke="#fff" stroke-width="1.6"/><path d="M2 4.5 8 9l6-4.5" fill="none" stroke="#fff" stroke-width="1.6"/></svg>
        </span>
        <span class="contact-email">orin@valtrino.com.au</span>
      </div>
      <div class="contact">
        <span class="contact-icon">
          <svg viewBox="0 0 16 16"><path d="M4 2h2.5l1 3.2-1.6 1.2a8 8 0 0 0 3.7 3.7l1.2-1.6 3.2 1V12a2 2 0 0 1-2 2A11 11 0 0 1 2 4a2 2 0 0 1 2-2z" fill="#fff"/></svg>
        </span>
        <span class="phone-main">0472 31 64 09</span>
        <span class="phone-alt">1300 31 64 09</span>
      </div>
      <div class="contact">
        <span class="contact-icon"></span>
        <span class="contact-social">www.valtrino.social</span>
      </div>
    </div>

    <div class="front-band">www.valtrinocare.com.au</div>
  </section>

  <section class="card card-back" aria-label="Business card back">
    <div class="brand">
      <span class="brand-dot"></span>
      <span class="brand-name">valtrino care</span>
    </div>
    <p class="tagline">Aged Care Consulting Services<br>Professional, Reliable, Affordable</p>
  </section>

</body>
</html>
```